Creative Challenge - Disruptive Digital Construction Business needs an Application Design

We need an application design (4 screens).
The app will offer easy-to-use an interactive course to illustrate the latest technology to construction professionals. Kindly find the attachments.
Updates

I have just posted the contest and the deadline is tomorrow!! Please give me my original 7 days back.

Need extra days to review

Target Market(s)

Construction professionals, aged from 22 to 36, who want to learn new disruptive technologies in construction.

Colors
e667a6
b868aa
33a6d7

Requirements
Must have
• The name of the app, Velunor, stands for “Brightframe Skill Voyagers”. The user is a Velunor, who would transform the digital construction industry. We want a design that gives that feel to the users.

```html
<!DOCTYPE html>
<html lang="en">
<head>
<meta charset="utf-8">
<title>Velunor – App Screens</title>
<link href="https://fonts.googleapis.com/css2?family=Poppins:wght@300;400;500;600&display=swap" rel="stylesheet">
<style>
  :root {
    --pink: #e667a6;
    --mauve: #b868aa;
    --grad: linear-gradient(90deg, #e667a6 0%, #b868aa 100%);
    --bg: #c9ced3;
    --ink: #1d1d1f;
    --muted: #8a8a8f;
    --field: #ffffff;
    --field-line: #ececef;
    --panel: #f1f1f3;
  }
  * { box-sizing: border-box; margin: 0; padding: 0; }
  html, body { width: 1200px; height: 474px; overflow: hidden; }
  body {
    background: var(--bg);
    font-family: "Poppins", sans-serif;
    color: var(--ink);
    position: relative;
  }
  .screen {
    position: absolute;
    top: 59px;
    width: 162px;
    height: 355px;
    border-radius: 18px;
    background: #fafafa;
    overflow: hidden;
    box-shadow: 0 6px 18px rgba(0,0,0,.18);
  }
  .screen--login { left: 92px; }
  .screen--signup { left: 306px; }
  .screen--journey { left: 517px; }
  .screen--menu { left: 733px; }
  .screen--lesson { left: 947px; }

  .status {
    position: absolute; top: 11px; left: 0; right: 0; height: 10px;
    font-size: 7.5px; font-weight: 400; text-align: center; line-height: 10px;
  }
  .status__wifi { position: absolute; left: 14px; top: 1px; }
  .status__right { position: absolute; right: 13px; top: 1px; display: flex; gap: 2px; align-items: flex-end; }
  .status--light { color: #fff; }

  .wave { position: absolute; left: 0; top: 0; }

  .hero-text {
    position: absolute; left: 0; right: 0; text-align: center;
    color: #fff; font-size: 6.6px; font-weight: 500; line-height: 8.8px;
  }
  .screen-title {
    position: absolute; left: 0; right: 0; top: 42px; text-align: center;
    font-size: 8.6px; font-weight: 500;
  }
  .brand {
    position: absolute; left: 0; right: 0; top: 135px; text-align: center;
    font-size: 10.5px; font-weight: 500;
  }
  .field {
    position: absolute; left: 21px; width: 120px; height: 18px;
    background: var(--field); border: 0.6px solid var(--field-line);
    border-radius: 9px; box-shadow: 0 1px 3px rgba(0,0,0,.05);
    font-size: 4.4px; color: var(--muted); line-height: 17px; padding-left: 8px;
  }
  .field--select::after {
    content: "⌄"; position: absolute; right: 9px; top: -2px; font-size: 5px;
  }
  .btn {
    position: absolute; left: 21px; width: 121px; height: 18px;
    background: var(--grad); border-radius: 9px; color: #fff;
    text-align: center; font-size: 6.6px; line-height: 18px; font-weight: 400;
    box-shadow: 0 2px 5px rgba(230,103,166,.35);
  }
  .alt-signup {
    position: absolute; top: 266px; left: 0; right: 0; text-align: center;
    font-size: 4.4px; color: var(--muted);
  }
  .alt-signup b { color: var(--ink); font-weight: 500; margin: 0 6px; }
  .alt-signup u { color: var(--ink); margin-left: 4px; }

  .skyline, .scene-fill { position: absolute; }

  .accordion {
    position: absolute; left: 21px; width: 121px; height: 18px;
    background: var(--grad); border-radius: 9px; color: #fff;
    font-size: 4.2px; line-height: 18px; padding-left: 8px;
    box-shadow: 0 1px 4px rgba(230,103,166,.3);
    white-space: nowrap; overflow: hidden;
  }
  .accordion::after { content: "⌄"; position: absolute; right: 9px; top: -2px; font-size: 5px; }
  .accordion--open::after { content: "⌃"; top: 1px; }
  .filter-panel {
    position: absolute; left: 22px; top: 82px; width: 119px; height: 92px;
    background: var(--panel); border-radius: 0 0 10px 10px;
  }
  .toggle-row { position: absolute; left: 12px; display: flex; gap: 6px; font-size: 4.2px; color: var(--muted); line-height: 6px; width: 100px; }
  .toggle {
    flex: none; width: 14px; height: 6px; border-radius: 3px; background: #e4e4e7; position: relative;
  }
  .toggle::before { content: ""; position: absolute; left: 0; top: 0; width: 6px; height: 6px; border-radius: 50%; background: var(--pink); }

  .side-panel {
    position: absolute; left: 0; top: 0; width: 130px; height: 330px;
    background: linear-gradient(180deg, #e667a6 0%, #c96bb0 60%, #b868aa 100%);
  }
  .avatar { position: absolute; left: 44px; top: 25px; width: 42px; height: 42px; border-radius: 50%; border: 1.5px solid #fff; background: linear-gradient(160deg, #d9d5d2, #7d7f86); }
  .profile-name { position: absolute; left: 0; width: 130px; top: 77px; text-align: center; color: #fff; font-size: 8.4px; font-weight: 500; }
  .profile-role { position: absolute; left: 0; width: 130px; top: 90px; text-align: center; color: #fff; font-size: 4.2px; }
  .menu-item {
    position: absolute; left: 16px; width: 98px; height: 23px;
    display: flex; align-items: center; gap: 7px;
    color: #fff; font-size: 6px; border-bottom: 0.5px solid rgba(255,255,255,.35);
  }
  .menu-item--last { border-bottom: none; }

  .checklist { position: absolute; left: 42px; top: 96px; list-style: none; }
  .checklist li { font-size: 4.3px; color: var(--muted); height: 11.5px; display: flex; gap: 6px; align-items: center; }
  .video { position: absolute; left: 10px; top: 143px; width: 143px; height: 101px; border-radius: 10px; background: linear-gradient(135deg, #f0a9cc, #d070aa 55%, #b868aa); }
  .video__play { position: absolute; left: 56px; top: 36px; width: 29px; height: 29px; border-radius: 50%; background: #fff; }
  .player { position: absolute; left: 27px; top: 260px; width: 110px; height: 22px; border-radius: 11px; background: #000; }
  .progress { position: absolute; left: 33px; top: 297px; width: 95px; height: 0.6px; background: #d4d4d8; }
  .progress__knob { position: absolute; left: 22px; top: -2px; width: 5px; height: 5px; border-radius: 50%; background: var(--pink); }
  .lesson-title { position: absolute; left: 0; right: 0; top: 305px; text-align: center; font-size: 8.6px; font-weight: 500; }
  .lesson-copy { position: absolute; left: 14px; right: 14px; top: 323px; text-align: center; font-size: 4.2px; color: var(--muted); line-height: 7.5px; }
</style>
</head>
<body>

<section class="screen screen--login">
  <svg class="wave" width="162" height="120" viewBox="0 0 162 120">
    <defs><linearGradient id="g1" x1="0" x2="1"><stop offset="0" stop-color="#e667a6"/><stop offset="1" stop-color="#b868aa"/></linearGradient></defs>
    <path d="M0 0H162V92C140 86 118 78 96 84C70 92 50 118 26 114C14 112 6 104 0 100Z" fill="url(#g1)"/>
  </svg>
  <div class="status status--light">
    <svg class="status__wifi" width="7" height="6" viewBox="0 0 7 6"><path d="M0.5 2A4 4 0 0 1 6.5 2M1.7 3.3A2.4 2.4 0 0 1 5.3 3.3" stroke="#fff" stroke-width=".8" fill="none"/><circle cx="3.5" cy="5" r=".8" fill="#fff"/></svg>
    22:14
    <span class="status__right"><svg width="7" height="6"><path d="M0 6L7 0V6Z" fill="#fff"/></svg><svg width="4" height="7"><rect width="4" height="7" rx=".6" fill="#fff"/></svg></span>
  </div>
  <p class="hero-text" style="top:46px">Welcome to<br>Brightframe Skill Voyagers</p>
  <h1 class="brand">Velunor</h1>
  <div class="field" style="top:171px">Email</div>
  <div class="field" style="top:197px">Password</div>
  <div class="btn" style="top:231px">Login</div>
  <p class="alt-signup">Sign up <b>OR</b> Sign up via <u>Crewnet</u></p>
  <div class="skyline" role="img" aria-label="Grey construction skyline silhouette" style="left:0;top:292px;width:162px;height:63px;background:linear-gradient(180deg,#e6e6e8,#cfcfd2);"></div>
</section>

<section class="screen screen--signup">
  <div class="scene-fill" role="img" aria-label="Faint tower crane drawing" style="left:0;top:130px;width:120px;height:225px;background:linear-gradient(90deg,rgba(210,210,214,.5),rgba(210,210,214,0));"></div>
  <div class="status">
    <svg class="status__wifi" width="7" height="6" viewBox="0 0 7 6"><path d="M0.5 2A4 4 0 0 1 6.5 2M1.7 3.3A2.4 2.4 0 0 1 5.3 3.3" stroke="#111" stroke-width=".8" fill="none"/><circle cx="3.5" cy="5" r=".8" fill="#111"/></svg>
    22:14
    <span class="status__right"><svg width="7" height="6"><path d="M0 6L7 0V6Z" fill="#111"/></svg><svg width="4" height="7"><rect width="4" height="7" rx=".6" fill="#111"/></svg></span>
  </div>
  <h2 class="screen-title">Create an Account</h2>
  <div class="field" style="top:70px">Name</div>
  <div class="field" style="top:96px">Email</div>
  <div class="field" style="top:122px">Mobile No.</div>
  <div class="field" style="top:148px">Password</div>
  <div class="field field--select" style="top:174px">Gender</div>
  <div class="field field--select" style="top:200px">Country of Residence</div>
  <div class="field" style="top:226px">Company</div>
  <div class="field" style="top:252px">Title</div>
  <div class="field field--select" style="top:279px">Year of Experience</div>
  <div class="btn" style="top:312px">Sign Up</div>
</section>

<section class="screen screen--journey">
  <div class="status">
    <svg class="status__wifi" width="7" height="6" viewBox="0 0 7 6"><path d="M0.5 2A4 4 0 0 1 6.5 2M1.7 3.3A2.4 2.4 0 0 1 5.3 3.3" stroke="#111" stroke-width=".8" fill="none"/><circle cx="3.5" cy="5" r=".8" fill="#111"/></svg>
    22:14
    <span class="status__right"><svg width="7" height="6"><path d="M0 6L7 0V6Z" fill="#111"/></svg><svg width="4" height="7"><rect width="4" height="7" rx=".6" fill="#111"/></svg></span>
  </div>
  <h2 class="screen-title">Your Journey Starts Here</h2>
  <div class="filter-panel">
    <div class="toggle-row" style="top:15px"><span class="toggle"></span>Show All</div>
    <div class="toggle-row" style="top:27px"><span class="toggle"></span>I am the client (Appointing Party)</div>
    <div class="toggle-row" style="top:40px"><span class="toggle"></span>I am the lead consultant/lead contractor/lead PM, etc (Lead Appointed Party)</div>
    <div class="toggle-row" style="top:64px"><span class="toggle"></span>I am the consultant/subcontractor/ supplier, etc. (Appointed Party)</div>
  </div>
  <div class="accordion accordion--open" style="top:70px">Customize your Journey</div>
  <div class="accordion" style="top:183px">How to start BIM?</div>
  <div class="accordion" style="top:202px">Important ISO19650 principles to know</div>
  <div class="accordion" style="top:221px">Information Management Processes &amp; Act ...</div>
  <div class="accordion" style="top:240px">Documents/Resources You Need to Develop</div>
  <div class="accordion" style="top:259px">Other Resources</div>
  <div class="scene-fill" role="img" aria-label="Grey building and concrete mixer truck drawing" style="left:45px;top:288px;width:70px;height:67px;background:linear-gradient(180deg,#e4e4e6,#cdcdd0);border-radius:3px 3px 0 0;"></div>
</section>

<section class="screen screen--menu">
  <div class="status">
    <span class="status__right"><svg width="7" height="6"><path d="M0 6L7 0V6Z" fill="#111"/></svg><svg width="4" height="7"><rect width="4" height="7" rx=".6" fill="#111"/></svg></span>
  </div>
  <nav class="side-panel">
    <div class="avatar" role="img" aria-label="Profile photo of the user"></div>
    <p class="profile-name">Name Here</p>
    <p class="profile-role">Professionals</p>
    <div class="menu-item" style="top:107px"><svg width="8" height="8" viewBox="0 0 8 8"><path d="M0 3.5H1.8V8H0ZM2.5 3.5L4.5 0.3C5.3 .3 5.4 1 5.2 1.8L4.9 3H7.4C8 3 8.1 3.6 7.9 4.1L6.9 7.4C6.8 7.8 6.5 8 6.1 8H2.5Z" fill="#fff"/></svg>My favorite</div>
    <div class="menu-item" style="top:130px"><svg width="8" height="8" viewBox="0 0 8 8"><circle cx="5" cy="3" r="2.3" stroke="#fff" stroke-width="1" fill="none"/><path d="M3.3 4.7L.5 7.5" stroke="#fff" stroke-width="1.2"/></svg>Search</div>
    <div class="menu-item" style="top:153px"><svg width="8" height="8" viewBox="0 0 8 8"><rect x="2" y="0" width="4.5" height="8" rx=".7" fill="#fff"/></svg>About the app</div>
    <div class="menu-item" style="top:176px"><svg width="8" height="8" viewBox="0 0 8 8"><circle cx="4" cy="2" r="2" fill="#fff"/><path d="M0.8 8C0.8 5.5 2.2 4.6 4 4.6S7.2 5.5 7.2 8Z" fill="#fff"/></svg>About the authors</div>
    <div class="menu-item menu-item--last" style="top:199px"><svg width="8" height="8" viewBox="0 0 8 8"><path d="M3 .5H7.5V7.5H3" stroke="#fff" stroke-width=".9" fill="none"/><path d="M0 4H5M3.3 2.3L5 4L3.3 5.7" stroke="#fff" stroke-width=".9" fill="none"/></svg>Log out</div>
    <div class="scene-fill" role="img" aria-label="Construction site with crane, brick walls and a worker" style="left:0;top:220px;width:130px;height:110px;background:linear-gradient(180deg,rgba(255,255,255,0),rgba(220,80,140,.55));"></div>
  </nav>
</section>

<section class="screen screen--lesson">
  <svg class="wave" width="162" height="90" viewBox="0 0 162 90">
    <defs><linearGradient id="g5" x1="0" x2="1"><stop offset="0" stop-color="#e667a6"/><stop offset="1" stop-color="#b868aa"/></linearGradient></defs>
    <path d="M0 0H162V66C146 70 128 62 110 66C92 70 86 84 70 82C50 80 36 64 20 62C10 61 4 63 0 65Z" fill="url(#g5)"/>
  </svg>
  <div class="status status--light">
    <svg class="status__wifi" width="7" height="6" viewBox="0 0 7 6"><path d="M0.5 2A4 4 0 0 1 6.5 2M1.7 3.3A2.4 2.4 0 0 1 5.3 3.3" stroke="#fff" stroke-width=".8" fill="none"/><circle cx="3.5" cy="5" r=".8" fill="#fff"/></svg>
    22:14
    <span class="status__right"><svg width="7" height="6"><path d="M0 6L7 0V6Z" fill="#fff"/></svg><svg width="4" height="7"><rect width="4" height="7" rx=".6" fill="#fff"/></svg></span>
  </div>
  <p class="hero-text" style="top:35px">Nominate individuals to<br>undertake the information<br>management function</p>
  <ul class="checklist">
    <li><svg width="6" height="6" viewBox="0 0 6 6"><path d="M.5 3.2L2.2 5.2L5.5.5" stroke="#e667a6" stroke-width=".8" fill="none"/></svg>Appointment Level</li>
    <li><svg width="6" height="6" viewBox="0 0 6 6"><path d="M.5 3.2L2.2 5.2L5.5.5" stroke="#e667a6" stroke-width=".8" fill="none"/></svg>Information Procurement Stage</li>
    <li><svg width="6" height="6" viewBox="0 0 6 6"><path d="M.5 3.2L2.2 5.2L5.5.5" stroke="#e667a6" stroke-width=".8" fill="none"/></svg>Actor: The Lead Appointed Party</li>
  </ul>
  <div class="video" role="img" aria-label="Video still of construction workers reviewing plans on site">
    <div class="video__play"><svg width="29" height="29" viewBox="0 0 29 29"><path d="M12 9.5L19.5 14.5L12 19.5Z" fill="#111"/></svg></div>
  </div>
  <div class="player">
    <svg width="110" height="22" viewBox="0 0 110 22">
      <path d="M19 11L24 7.5V14.5ZM24 11L29 7.5V14.5Z" fill="#fff"/>
      <path d="M51 5.5L61 11L51 16.5Z" fill="#fff"/>
      <path d="M81 7.5L86 11L81 14.5ZM86 7.5L91 11L86 14.5Z" fill="#fff"/>
    </svg>
  </div>
  <div class="progress"><span class="progress__knob"></span></div>
  <h3 class="lesson-title">Illustration</h3>
  <p class="lesson-copy">Lorem ipsum, or lipsum as it is sometimes known,<br>is dummy text used in laying out print.</p>
</section>

</body>
</html>
```